Lorival Brisk a young drag queen needs a website to promote herself

URLs: queenlorival.com / lorivalbrisk.com
General Requests
• SEO-Optimized
• CMS: Joomla
Lorival Brisk is a young Drag queen still going to college and living in the us. She has an international Background with Canadian and Swiss citizenship. She is very creative not only in her Shows but she is also a painter, a Fashion designer a Music writer, a singer and an excellent vegan cook.

In order to promote her and to book her for a Show or a maquillage she needs a Website that will highly interact with social Media.

The Structure of the Website could be as follows:

Welcome page
From the Welcome page navigation to
1. Blog
a. Easy tool to add new Blogs
b. Possibility for others to write comments
c. Possibilty to
2. Events: Videos and Pictures
a. Easy Way to Ad Pictures and Vidoes and Showing a Title/Description
3. Upcoming Events and Shows
a. Possibility to describe Upcoming shows with link for more Information and Registration
4. Book a Show
a. I offer a lot of different Shows with Dancing, Singing or Moderating an Evening. Since I Speak English, (Swiss-)German and French I can entertain a multicultural Audience. Just get in touch with me and let’s discuss it.
b. Contact form for ordering an offer for a show (Name and Address; Kind of Show, Duration, Date, Place, Budget, Captcha)
c. lorival@lorivalbrisk.com
5. Book a Maquillage
a. Do you want to look like a Drag? Are you a young Drag and want to learn how to get dressed up an a unique Maquillage? Do you want to have a special surprise for a Bachelors Party? Just ask me! I’m your Expert! Also available as Gift Certificate.
b. Contact form for ordering an offer for a Maquillage (Name and Address; Kind of Maquillage, Option for Gift Certificate; Occasion, Date, Place, Budget; captcha);
c. Form mailed to lorival@lorivalbrisk.com
6. Lorival on Social Media
a. Join me on Pagewall
b. Join me on Pictora
c. Join me on Tunedrift
7. Sponsors and Partners
a. Mesa Unity Collective
b. ….
Updates

Industry/Entity Type

College

Number of Pages Required

5+ page

Font styles to use
Decorative

Colors
6b449b
d2a4cc
e4daeb

Requirements
Must have
• Responsive Design

```html
<!DOCTYPE html>
<html lang="en">
<head>
<meta charset="utf-8">
<title>Lorival Brisk — Drag Queen, Shows &amp; Maquillage</title>
<link rel="stylesheet" href="https://fonts.googleapis.com/css2?family=Mulish:wght@400;600;700;800&display=swap">
<style>
:root{
  --teal:#13a08a;
  --teal-dark:#0f8a76;
  --ink:#3a3a3a;
  --muted:#666;
  --line:#dedede;
  --band:#f4f4f4;
  --white:#fff;
  --panel:rgba(18,14,10,.88);
  --field:#2a2520;
  --field-line:#4a423a;
}
*{box-sizing:border-box;margin:0;padding:0}
html,body{width:1200px;height:2517px;overflow:hidden}
body{position:relative;background:var(--white);font-family:"Mulish",Arial,sans-serif;color:var(--ink)}
.abs{position:absolute}

/* header */
.site-header{left:0;top:0;width:1200px;height:84px}
.brand{left:117px;top:24px;font-size:29px;font-weight:800;color:var(--teal);letter-spacing:-.3px}
.main-nav{left:333px;top:36px;display:flex;gap:20px;font-size:12.5px;font-weight:600;color:#222}

/* hero */
.hero{left:0;top:84px;width:1200px;height:522px;background:linear-gradient(120deg,#8a6a44 0%,#b08a5c 30%,#7a5a3a 60%,#a07c52 100%)}
.hero-figure{left:470px;top:0;width:360px;height:522px;background:radial-gradient(ellipse at 50% 55%,#c79a3a 0%,rgba(160,110,40,.6) 40%,rgba(0,0,0,0) 70%)}
.hero-dots{left:572px;top:561px;display:flex;gap:10px}
.hero-dots span{width:8px;height:8px;border-radius:50%;background:#fff}
.hero-dots span.on{background:#222}

.booking-panel{left:846px;top:118px;width:260px;height:447px;background:var(--panel);padding:18px 14px}
.booking-panel h2{font-size:20px;font-weight:700;color:#fff;margin-bottom:14px}
.field{width:232px;height:32px;background:var(--field);border:1px solid var(--field-line);border-radius:2px;margin-bottom:10px;font-size:10px;color:#776d62;padding:8px 8px;font-style:italic}
.field.tall{height:66px;margin-bottom:12px}
.captcha-row{display:flex;align-items:center;justify-content:space-between;margin-top:2px}
.captcha-row label{font-size:11px;font-weight:700;color:#fff}
.captcha-row .field{width:162px;margin:0}
.btn-submit{display:inline-block;margin-top:20px;background:var(--teal);color:#fff;font-size:14px;font-weight:700;padding:5px 14px;border-radius:2px}

/* welcome */
.welcome-title{left:0;top:654px;width:1200px;text-align:center;font-size:15px;font-weight:800;letter-spacing:.4px}
.welcome-text{left:95px;top:697px;width:1010px;text-align:center;font-size:13.5px;line-height:24px;color:#444}
.btn-primary{left:517px;top:778px;width:166px;height:47px;background:var(--teal);color:#fff;font-size:15px;font-weight:700;display:flex;align-items:center;justify-content:center;border-radius:2px}

/* blog */
.section-head{border-top:1px solid var(--line);border-bottom:1px solid var(--line);height:57px;display:flex;align-items:center;justify-content:space-between;font-size:15px;font-weight:800}
.blog-head{left:93px;top:896px;width:667px}
.events-head{left:786px;top:896px;width:321px}
.carousel-arrows{display:flex;gap:16px;margin-right:4px}
.blog-post{left:93px;width:667px}
.blog-thumb{position:absolute;left:0;top:0;width:233px;height:140px}
.blog-body{position:absolute;left:247px;top:14px;width:420px;font-size:11.5px;line-height:21px;color:#555}
.blog-body strong{display:block;color:#222;font-weight:800}
.blog-meta{position:absolute;left:0;top:171px;width:667px;height:54px;border-top:1px solid var(--line);border-bottom:1px solid var(--line);display:flex;align-items:center;justify-content:space-between}
.comments{font-size:12px;font-weight:700;color:var(--teal);display:flex;align-items:center;gap:5px}
.btn-small{background:var(--teal);color:#fff;font-size:11.5px;font-weight:700;padding:6px 9px;border-radius:2px}

/* events */
.event{left:786px;width:321px;height:110px}
.event-date{position:absolute;left:0;top:0;width:73px;height:62px;background:var(--teal);color:#fff;text-align:center}
.event-date .day{display:block;font-size:11px;font-weight:700;margin-top:9px}
.event-date .year{display:block;font-size:22px;font-weight:700;line-height:24px}
.event-text{position:absolute;left:94px;top:0;width:227px;font-size:11.5px;line-height:21.5px;color:#555}
.event-text strong{display:block;color:#222;font-weight:800}
.event-text b{color:#222}
.btn-more{left:786px;top:1448px;width:320px;height:37px;background:#ececec;display:flex;align-items:center;justify-content:center;font-size:11.5px;font-weight:800;color:#333}

/* gallery */
.section-title{width:1200px;left:0;text-align:center;font-size:26px;font-weight:600;color:#555}
.gallery-frame{left:265px;top:1648px;width:668px;height:330px;background:radial-gradient(ellipse at 45% 45%,#3d5f86 0%,#1b2a3a 45%,#0f1822 100%)}
.gallery-shadow{left:290px;top:1972px;width:620px;height:44px;background:radial-gradient(ellipse at 50% 0%,rgba(0,0,0,.28) 0%,rgba(0,0,0,0) 70%)}
.gallery-arrow{top:1800px}

/* social */
.social-band{left:0;top:2045px;width:1200px;height:367px;background:var(--band)}
.social-item{top:2188px;width:300px;text-align:center}
.social-item .disc{width:108px;height:108px;border-radius:50%;margin:0 auto 24px}
.social-item p{font-size:21px;color:#555}

/* footer */
.footer-nav{left:0;top:2444px;width:1200px;display:flex;justify-content:center;gap:18px;font-size:12px;font-weight:600;color:#222}
.footer-nav .sep{color:#444}
.copyright{left:0;top:2480px;width:1200px;text-align:center;font-size:11.5px;font-weight:700;color:#222}
</style>
</head>
<body>

<header class="site-header abs">
  <div class="brand abs">Lorivalbrisk</div>
  <nav class="main-nav abs">
    <span>Home</span><span>Blog</span><span>Events</span><span>Book a Show</span><span>Book a Maquillage</span><span>Lorival on Social Media</span><span>Sponsors &amp; Partners</span><span>Contact us</span>
  </nav>
</header>

<section class="hero abs" role="img" aria-label="Photo of Lorival Brisk in a golden sequined gown standing among sandstone rocks">
  <div class="hero-figure abs"></div>
</section>
<div class="hero-dots abs"><span class="on"></span><span></span><span></span><span></span></div>

<form class="booking-panel abs">
  <h2>Book A Show</h2>
  <div class="field tall">Name and Address</div>
  <div class="field">Kind of Show</div>
  <div class="field">Duration</div>
  <div class="field">Date</div>
  <div class="field">Place</div>
  <div class="field">Budget</div>
  <div class="captcha-row"><label>Catpcha</label><div class="field"></div></div>
  <span class="btn-submit">Submit</span>
</form>

<h1 class="welcome-title abs">WELCOME TO LORIVAL BRISK</h1>
<p class="welcome-text abs">Lorival Brisk is a young Drag queen still going to college and living in the us. She has an international Background with Canadian and Swiss citizenship. She is very creative not only in her Shows but she is also a painter, a Fashion designer a Music writer, a singer and an excellent vegan cook.</p>
<div class="btn-primary abs">BOOK A SHOW</div>

<div class="section-head blog-head abs">
  <span>BLOG</span>
  <span class="carousel-arrows">
    <svg width="9" height="14" viewBox="0 0 9 14"><path d="M7 1 1 7l6 6" fill="none" stroke="#999" stroke-width="2"/></svg>
    <svg width="9" height="14" viewBox="0 0 9 14"><path d="M2 1l6 6-6 6" fill="none" stroke="#999" stroke-width="2"/></svg>
  </span>
</div>
<div class="section-head events-head abs"><span>UPCOMING EVENTS AND SHOWS</span></div>

<article class="blog-post abs" style="top:997px">
  <div class="blog-thumb" role="img" aria-label="Portrait of Lorival in stage makeup with a black top hat" style="background:linear-gradient(90deg,#4a4a4a,#bdbdbd 55%,#e8e8e8)"></div>
  <div class="blog-body"><strong>Lorem Ipsum is simply dummy text of the printing and typesetting industry. Lorem Ipsum has been the industry's standard</strong>Since the 1500s, when an unknown printer took a galley of type and scrambled it to make a type specimen book. It has survived not only five centuries, but also the leap into electronic typesetting, remaining essentially unchanged.</div>
  <div class="blog-meta">
    <span class="comments"><svg width="12" height="10" viewBox="0 0 12 10"><path d="M6 0C2.7 0 0 1.9 0 4.3c0 1.2.7 2.3 1.9 3L1.4 10l3-1.9c.5.1 1 .2 1.6.2 3.3 0 6-1.9 6-4.3S9.3 0 6 0z" fill="#333"/></svg>Comments</span>
    <span class="btn-small">Read More</span>
  </div>
</article>

<article class="blog-post abs" style="top:1258px">
  <div class="blog-thumb" role="img" aria-label="Portrait of Lorival with blue hair and glittering makeup" style="background:linear-gradient(90deg,#2a2530,#5a4a70 45%,#3a3440)"></div>
  <div class="blog-body"><strong>Lorem Ipsum is simply dummy text of the printing and typesetting industry. Lorem Ipsum has been the industry's standard</strong>Since the 1500s, when an unknown printer took a galley of type and scrambled it to make a type specimen book. It has survived not only five centuries, but also the leap into electronic typesetting, remaining essentially unchanged.</div>
  <div class="blog-meta">
    <span class="comments"><svg width="12" height="10" viewBox="0 0 12 10"><path d="M6 0C2.7 0 0 1.9 0 4.3c0 1.2.7 2.3 1.9 3L1.4 10l3-1.9c.5.1 1 .2 1.6.2 3.3 0 6-1.9 6-4.3S9.3 0 6 0z" fill="#333"/></svg>Comments</span>
    <span class="btn-small">Read More</span>
  </div>
</article>

<article class="event abs" style="top:996px">
  <div class="event-date"><span class="day">June 3rd</span><span class="year">2015</span></div>
  <div class="event-text"><strong>Lorem Ipsum is simply dummy text of the printing and typesetting .</strong>Since the 1500s, when an unknown printer took a galley of type and scrambled... <b>Read More</b></div>
</article>
<article class="event abs" style="top:1157px">
  <div class="event-date"><span class="day">June 3rd</span><span class="year">2015</span></div>
  <div class="event-text"><strong>Lorem Ipsum is simply dummy text of the printing and typesetting .</strong>Since the 1500s, when an unknown printer took a galley of type and scrambled... <b>Read More</b></div>
</article>
<article class="event abs" style="top:1318px">
  <div class="event-date"><span class="day">June 3rd</span><span class="year">2015</span></div>
  <div class="event-text"><strong>Lorem Ipsum is simply dummy text of the printing and typesetting .</strong>Since the 1500s, when an unknown printer took a galley of type and scrambled... <b>Read More</b></div>
</article>
<div class="btn-more abs">VIEW MORE UPCOMING EVENTS</div>

<h2 class="section-title abs" style="top:1588px">Photo Gallery</h2>
<div class="gallery-shadow abs"></div>
<div class="gallery-frame abs" role="img" aria-label="Photo of Lorival with blue hair in a white bodysuit surrounded by soap bubbles on a dark background"></div>
<svg class="gallery-arrow abs" style="left:286px" width="16" height="26" viewBox="0 0 16 26"><path d="M13 2 3 13l10 11" fill="none" stroke="#fff" stroke-width="4"/></svg>
<svg class="gallery-arrow abs" style="left:896px" width="16" height="26" viewBox="0 0 16 26"><path d="M3 2l10 11L3 24" fill="none" stroke="#fff" stroke-width="4"/></svg>

<section class="social-band abs"></section>
<h2 class="section-title abs" style="top:2095px">Lorival on Social Media</h2>
<div class="social-item abs" style="left:137px"><div class="disc" style="background:#3b5998"></div><p>Join me on Pagewall</p></div>
<div class="social-item abs" style="left:465px"><div class="disc" style="background:#517fa4"></div><p>Join me on Pictora</p></div>
<div class="social-item abs" style="left:822px"><div class="disc" style="background:#ff5500"></div><p>Join me on Tunedrift</p></div>

<nav class="footer-nav abs">
  <span>Home</span><span class="sep">|</span><span>Blog</span><span class="sep">|</span><span>Events</span><span class="sep">|</span><span>Book a Show</span><span class="sep">|</span><span>Book a Maquillage</span><span class="sep">|</span><span>Lorival on Social Media</span><span class="sep">|</span><span>Sponsors &amp; Partners</span><span class="sep">|</span><span>Contact us</span>
</nav>
<p class="copyright abs">© 2015 &nbsp;Company Name , All Rights Reserved</p>

</body>
</html>
```